Book Cover Design Project - SIMPLE ART, Pre-Concepted

We already have a full design concept for the cover art. It is however in a low quality word document format. This project is to recreate existing example guideline art in as much vector art possible for great quality print production. Artistic flare is welcome. This will be for a book cover (front/back) and I want the quality to be excellent.

Art to be provided in Adobe Illustrator format. The book will be 6wide x 9high, so the artboard for the cover needs to be set up to 12.5 wide x 9 high with .125" bleeds.

Copy content for the spine: "Beneath the Orchard Lamps at Dusk" RL Ombrisko.

Here is a link to download the word document "template" and a new photo for the back page. I'm not sure that I like the new photo, it is possible the old one in the word document will work.

www.kelmarpressworks.com/uploads/BriefingFilesSetAll.zip

I've got a fast deadline on this project because the client would like to have manufacturing completed by Christmas...which is why this is only a 2 day project. I appreciate your interest in our project.

Gordon

Try this link...seems I was missing the .zip extension which may have been causing problems.

Requirements
Must have
• Adobe Illustrator Files
CMYK color setup - no color definitions for project
Artboard Size: 12.625 wide x 9.125 high
Art Orientation: Flat image should have the back book page on the left side, front page on the right side, spine copy running down the middle.

```html
<!DOCTYPE html>
<html lang="en">
<head>
<meta charset="utf-8">
<title>Beneath the Orchard Lamps at Dusk — Cover</title>
<link rel="stylesheet" href="https://fonts.googleapis.com/css2?family=Josefin+Sans:wght@400;600&display=swap">
<style>
  :root {
    --sky-dark: #1c1c1c;
    --sky-mid: #6e6e6e;
    --sky-light: #d9d9d9;
    --sky-glow: #ffffff;
    --cross: #000000;
    --cross-edge: #3a3a3a;
    --type: #ffffff;
  }
  html, body {
    margin: 0;
    padding: 0;
    width: 1200px;
    height: 867px;
    overflow: hidden;
    background: var(--sky-dark);
  }
  .cover {
    position: relative;
    width: 1200px;
    height: 867px;
    overflow: hidden;
  }
  .cover__art {
    position: absolute;
    inset: 0;
    width: 1200px;
    height: 867px;
    display: block;
  }
  .cover__title {
    position: absolute;
    left: 802px;
    top: 509px;
    margin: 0;
    font-family: "Josefin Sans", sans-serif;
    font-weight: 600;
    font-variant: small-caps;
    font-size: 31px;
    line-height: 39.5px;
    letter-spacing: 2px;
    color: var(--type);
  }
  .cover__title span { display: block; }
  .cover__byline {
    position: absolute;
    left: 805px;
    top: 770px;
    margin: 0;
    font-family: "Josefin Sans", sans-serif;
    font-weight: 600;
    font-variant: small-caps;
    font-size: 13px;
    letter-spacing: 1.4px;
    color: var(--type);
  }
</style>
</head>
<body>
  <main class="cover">
    <svg class="cover__art" viewBox="0 0 1200 867" xmlns="http://www.w3.org/2000/svg">
      <defs>
        <linearGradient id="skyBase" x1="0" y1="0" x2="1" y2="0">
          <stop offset="0" stop-color="var(--sky-dark)"/>
          <stop offset="0.35" stop-color="#3d3d3d"/>
          <stop offset="0.6" stop-color="var(--sky-light)"/>
          <stop offset="1" stop-color="#8a8a8a"/>
        </linearGradient>
        <radialGradient id="skyGlow" cx="0.5" cy="0.28" r="0.45">
          <stop offset="0" stop-color="var(--sky-glow)" stop-opacity="1"/>
          <stop offset="0.5" stop-color="var(--sky-glow)" stop-opacity="0.55"/>
          <stop offset="1" stop-color="var(--sky-glow)" stop-opacity="0"/>
        </radialGradient>
        <linearGradient id="skyFloor" x1="0" y1="0" x2="0" y2="1">
          <stop offset="0.45" stop-color="#000" stop-opacity="0"/>
          <stop offset="1" stop-color="#000" stop-opacity="0.45"/>
        </linearGradient>
        <linearGradient id="lightBeam" x1="0" y1="0" x2="1" y2="0">
          <stop offset="0" stop-color="#fff" stop-opacity="0"/>
          <stop offset="0.5" stop-color="#fff" stop-opacity="0.5"/>
          <stop offset="1" stop-color="#fff" stop-opacity="0"/>
        </linearGradient>
      </defs>

      <g class="sky" role="img" aria-label="Black and white photograph of a cloudy sky with sunbeams breaking through">
        <rect width="1200" height="867" fill="url(#skyBase)"/>
        <rect width="1200" height="867" fill="url(#skyGlow)"/>
        <rect x="440" y="300" width="320" height="567" fill="url(#lightBeam)"/>
        <rect width="1200" height="867" fill="url(#skyFloor)"/>
      </g>

      <g class="cross">
        <path class="cross__upright" fill="var(--cross)"
              d="M558 76 Q600 62 642 76 L642 782 Q600 796 558 782 Z"/>
        <path class="cross__edge" fill="none" stroke="#ffffff" stroke-width="1.5"
              d="M643 330 L643 782"/>
        <path class="cross__beam" fill="var(--cross)"
              d="M402 254 L798 254 Q806 292 798 330 L402 330 Q394 292 402 254 Z"/>
        <path class="cross__beam-shade" fill="var(--cross-edge)"
              d="M404 318 L796 318 Q798 324 798 330 L402 330 Q402 324 404 318 Z"/>
      </g>
    </svg>

    <h1 class="cover__title">
      <span>Beneath the</span>
      <span>Orchard Lamps</span>
      <span>at Dusk</span>
    </h1>
    <p class="cover__byline">A compilation of poems by RL Ombrisko</p>
  </main>
</body>
</html>
```